Design a professional business card with 2 URLs

We are looking for a professional & artistic way to integrate our new website to the business card. To explain this in more detail, "[url removed, login to view]" is the mother company, and we recently developed a website call "[url removed, login to view]". We want a natural way to include the new website's logo (or maybe just the URL) to the card, but not confusing people to think it is 2 different companies.

1) We want to keep the [url removed, login to view] company logo design (attached 2 velpins logo files), so do NOT need to change this.
2) We also want to keep the [url removed, login to view] product logo ([url removed, login to view]), but we flexible where you place the logo or URL on the card
3) Attached our current business card as a reference (biz card). This you can change the layout/design/font, we trust your artistic taste
4) The URLs for reference, you can also visit the site to understand our theme and what we do.
Company URL: [url removed, login to view]
Product URL: [url removed, login to view]

** The card dimension will be 54mm x 90mm.
We prefer landscape, but if you have portrait design that works, we will consider as well.

```html
<!DOCTYPE html>
<html lang="en">
<head>
<meta charset="utf-8">
<title>velpins – business card</title>
<link href="https://fonts.googleapis.com/css2?family=Arimo:wght@400&display=swap" rel="stylesheet">
<style>
  :root {
    --backdrop: #e4e3e6;
    --card: #5e5a72;
    --ink: #ffffff;
  }
  * { margin: 0; padding: 0; box-sizing: border-box; }
  html, body {
    width: 1200px;
    height: 1176px;
    overflow: hidden;
    background: var(--backdrop);
  }
  .canvas {
    position: relative;
    width: 1200px;
    height: 1176px;
  }
  .card {
    position: absolute;
    left: 200px;
    width: 780px;
    height: 446px;
    background: var(--card);
    color: var(--ink);
    font-family: "Arimo", Arial, sans-serif;
    font-weight: 400;
  }
  .card--front { top: 55px; }
  .card--back { top: 605px; }

  .brand {
    position: absolute;
    left: 0;
    width: 100%;
    height: 90px;
    text-align: center;
    font-size: 66px;
    line-height: 90px;
    white-space: nowrap;
  }
  .card--front .brand { top: 33px; }
  .card--back .brand { top: 179px; }

  .holder {
    position: absolute;
    left: 59px;
    width: 340px;
    top: 218px;
    line-height: 40px;
    font-size: 34px;
    text-align: center;
    white-space: nowrap;
  }
  .divider {
    position: absolute;
    left: 391px;
    top: 172px;
    width: 2px;
    height: 140px;
    background: var(--ink);
  }
  .contact {
    position: absolute;
    left: 431px;
    top: 176px;
    list-style: none;
    font-size: 25px;
    line-height: 33.4px;
    white-space: nowrap;
  }
  .address {
    position: absolute;
    left: 0;
    width: 100%;
    top: 350px;
    text-align: center;
    font-size: 21px;
    line-height: 32px;
    white-space: nowrap;
  }
  .links {
    position: absolute;
    left: 0;
    width: 100%;
    top: 336px;
    list-style: none;
    text-align: center;
    font-size: 23px;
    line-height: 32px;
  }
</style>
</head>
<body>
  <main class="canvas">
    <section class="card card--front" aria-label="Business card front">
      <div class="brand">velpins</div>
      <p class="holder">MARCUS LEUNG</p>
      <span class="divider"></span>
      <ul class="contact">
        <li>+852 61837409</li>
        <li>marcus@velpins.io</li>
        <li>https://www.velpins.io</li>
        <li>https://www.trovia.com/</li>
      </ul>
      <p class="address">
        Unit 412-417, 4/F, Harbour Innovation Hub,No. 8 Lakeside Road , East Wing<br>
        Tai Po Technology Park, Tai Po, N. T. ,Hong Kong
      </p>
    </section>

    <section class="card card--back" aria-label="Business card back">
      <div class="brand">velpins</div>
      <ul class="links">
        <li>https://www.velpins.io</li>
        <li>https://www.trovia.com/</li>
      </ul>
    </section>
  </main>
</body>
</html>
```